Business Card Design

I'm looking for a cool business card design that showcases what my company does... I am the owner and Brava is a play on my last name. The Brava Group is a privately held entity that specializes in media (Brava Media) and financial services (Brava Trading).

Brava Media focuses on the distribution and management of quality entertainment properties to all areas of the media world including broadcast, cable, digital, mobile and social media. Brava Media helps media and entertainment companies create and market great content and ensure that it reaches the widest audience possible.

Brava Media currently represents Ripple TV (www.rippletv-example.com), the fastest growing over the air broadcast network that focuses on programming that appeals to the African American audience. Brava Media also represents two new over the air broadcast networks launching in Summer 2014 - Harbor TV (www.harbortv-example.com) and Maple TV (www.mapletv-example.com).

Brava Media is an investor and business partner in SunDrift (www.sundrift-example.com) - a mobile social platform that empowers the user to choose how long your photos and videos live online.

Brava Media also represents KRN Enterprises (www.krnent-example.com), an independent producer that creates talent-driven and cost-effective programming around emerging talent and Clearbrook Content, a prolific producer of multimedia content including QXN's hit program - Velvet Hall.

Brava Trading manages a family office and focuses on building meaningful partnerships with all major financial institutions with a heavy concentration on IPO and secondary offerings.

Industry/Entity Type

Entertainment

Contact Information for Business Card

Martin Hale
12 Cobalt Lane
Roslyn New York 11492
O 555.555.0143
C 555.555.0178

```html
<!DOCTYPE html>
<html lang="en">
<head>
<meta charset="utf-8">
<title>The Brava Group – Business Card</title>
<link rel="stylesheet" href="https://fonts.googleapis.com/css2?family=Source+Sans+3:wght@400;600&display=swap">
<style>
  :root {
    --page-bg: #f4f4f4;
    --card-dark: #3d3d3d;
    --card-dark-shade: #353535;
    --card-light: #ffffff;
    --brand-orange: #e07f24;
    --brand-grey: #736e66;
    --brand-cream: #ece3c4;
    --text-dark: #2f2f2f;
  }
  * { box-sizing: border-box; margin: 0; padding: 0; }
  html, body {
    width: 1200px;
    height: 675px;
    overflow: hidden;
    background: var(--page-bg);
    font-family: "Source Sans 3", Arial, sans-serif;
  }
  .stage {
    position: relative;
    width: 1200px;
    height: 675px;
  }
  .card {
    position: absolute;
    top: 188px;
    width: 520px;
    height: 298px;
    overflow: hidden;
    box-shadow: 0 6px 16px rgba(0, 0, 0, 0.18);
  }
  .card--back {
    left: 60px;
    background: var(--card-dark);
  }
  .card--front {
    left: 620px;
    background: var(--card-light);
  }

  /* Back side */
  .back__motif {
    position: absolute;
    left: 30px;
    top: 0;
    width: 150px;
    height: 298px;
    background: radial-gradient(ellipse at 50% 40%, var(--card-dark-shade) 0%, var(--card-dark) 72%);
  }
  .brand {
    position: absolute;
    display: flex;
    align-items: center;
    gap: 12px;
  }
  .brand__dot {
    width: 46px;
    height: 46px;
    border-radius: 50%;
    background: var(--brand-cream);
    flex: none;
  }
  .brand__name {
    font-weight: 600;
    font-size: 30px;
    line-height: 1;
    letter-spacing: 0.5px;
    white-space: nowrap;
    color: var(--brand-orange);
  }
  .card--back .brand {
    left: 150px;
    top: 110px;
  }

  /* Front side */
  .card--front .brand {
    right: 34px;
    top: 72px;
  }
  .contact {
    position: absolute;
    left: 38px;
    top: 140px;
    color: var(--text-dark);
    font-size: 13px;
    line-height: 19px;
  }
  .contact__name {
    color: var(--brand-orange);
    font-size: 18px;
    line-height: 22px;
    margin-bottom: 6px;
  }
  .footer-bands {
    position: absolute;
    left: 0;
    right: 0;
    bottom: 0;
    height: 20px;
    display: flex;
    gap: 4px;
  }
  .footer-bands__grey {
    flex: 0 0 64%;
    background: var(--brand-grey);
  }
  .footer-bands__orange {
    flex: 1;
    background: var(--brand-orange);
  }
</style>
</head>
<body>
<main class="stage">
  <section class="card card--back" aria-label="Card back">
    <div class="back__motif" role="img" aria-label="Faint howling wolf silhouette"></div>
    <div class="brand">
      <span class="brand__dot"></span>
      <span class="brand__name">The Brava Group</span>
    </div>
  </section>

  <section class="card card--front" aria-label="Card front">
    <div class="contact">
      <p class="contact__name">Martin Hale</p>
      <p>12 Cobalt Lane</p>
      <p>Alder Falls, Oregon 97999</p>
      <p>Phone: 555.555.0143</p>
      <p>Cellphone: 555.555.0178</p>
    </div>
    <div class="brand">
      <span class="brand__dot"></span>
      <span class="brand__name">The Brava Group</span>
    </div>
    <div class="footer-bands">
      <span class="footer-bands__grey"></span>
      <span class="footer-bands__orange"></span>
    </div>
  </section>
</main>
</body>
</html>
```